Bows Catalog Cover

Cover Page for a catalog for bows. Same logo KOR Atelier Nordique Archetiers.
Catalog overview: https://www.folioprinthub.com/KOR-Atelier-Nordique-Archetiers/catalogs/KOR-catalog.html
No instruments, no scores, Only bows or bow parts (head, frog ...). Drawings or pictures.

Target Market(s)

Violin makers and reseller

Requirements
Must have
• bows or bow parts
Nice to have
• Drawings and or pictures
Should not have
• full Instruments or scores

```html
<!DOCTYPE html>
<html lang="en">
<head>
<meta charset="utf-8">
<title>KOR Atelier Nordique Archetiers — Catalog</title>
<link href="https://fonts.googleapis.com/css2?family=Kaushan+Script&family=Michroma&display=swap" rel="stylesheet">
<style>
  :root {
    --paper: #f6f5f3;
    --violet: #9c2489;
    --indigo: #2e3586;
    --brand: #5a2c8c;
    --white: #ffffff;
    --wood: #7b2f25;
    --hair: #e8dcc0;
  }
  html, body {
    margin: 0;
    padding: 0;
    overflow: hidden;
    background: var(--paper);
  }
  .cover {
    position: relative;
    width: 927px;
    height: 1200px;
    overflow: hidden;
    background: var(--paper);
  }
  .cover-art {
    position: absolute;
    inset: 0;
    width: 927px;
    height: 1200px;
  }
  .brand {
    position: absolute;
    top: 78px;
    left: 342px;
    display: flex;
    align-items: center;
    gap: 22px;
  }
  .brand-mark {
    width: 128px;
    height: 128px;
    border-radius: 50%;
    background: var(--brand);
    flex: none;
  }
  .brand-text {
    display: flex;
    flex-direction: column;
    color: var(--brand);
    font-family: "Michroma", sans-serif;
    font-weight: 400;
  }
  .brand-name {
    font-size: 92px;
    line-height: 1;
    letter-spacing: 14px;
  }
  .brand-full {
    margin-top: 14px;
    font-size: 11.5px;
    letter-spacing: 1.6px;
    white-space: nowrap;
  }
  .cover-title {
    position: absolute;
    left: 62px;
    top: 870px;
    margin: 0;
    color: var(--white);
    font-family: "Kaushan Script", cursive;
    font-weight: 400;
    font-size: 158px;
    line-height: 1;
  }
</style>
</head>
<body>
  <main class="cover">
    <svg class="cover-art" viewBox="0 0 927 1200" aria-hidden="false">
      <defs>
        <linearGradient id="panelGradient" x1="0" y1="0" x2="0" y2="1">
          <stop offset="0" stop-color="var(--violet)"/>
          <stop offset="1" stop-color="var(--indigo)"/>
        </linearGradient>
        <linearGradient id="bowGradient" x1="0" y1="0" x2="1" y2="1">
          <stop offset="0" stop-color="#8a4a3c"/>
          <stop offset="0.5" stop-color="#b98d70"/>
          <stop offset="1" stop-color="var(--hair)"/>
        </linearGradient>
      </defs>
      <polygon class="colour-panel" points="0,0 8,0 727,1200 0,1200" fill="url(#panelGradient)"/>
      <polygon class="bow-photo" role="img"
        aria-label="Photograph of a violin bow lying diagonally, showing its brown stick, ebony frog with pearl eye and pale horsehair"
        points="520,328 578,328 727,560 927,1020 927,1200 884,1200 690,760 520,360"
        fill="url(#bowGradient)" opacity="0.55"/>
    </svg>

    <header class="brand">
      <div class="brand-mark"></div>
      <div class="brand-text">
        <span class="brand-name">KOR</span>
        <span class="brand-full">ATELIER NORDIQUE ARCHETIERS</span>
      </div>
    </header>

    <h1 class="cover-title">Catalog</h1>
  </main>
</body>
</html>
```